Logo für eine Distribution/Handelsunternehmung
Zielgruppe
Wir vertrieben Produkte aus der Audio-, Vieo- und Medientechnik. Die Produkte der Distribution sind ausschließlich für den professionellen Handel bestimmt. Die Produkte des Handelsunternehmens sind für professionelle Endanwender, Firmen und Institutionen bestimmt.
Aufgabenstellung
Bei dem Logodesign bin ich nicht festgelegt. Das Logo soll frisch und modern wirken, aber nicht zu verspielt oder unseriös. Das neue Unternehmen soll dadurch zwr präsent aber nicht aufdringlich wirken. Das Logo soll sowohl im Web wie auch im Print gut zur Geltung kommen.

```html
<!DOCTYPE html>
<html lang="de">
<head>
<meta charset="utf-8">
<title>Talvera – Geschäftsausstattung</title>
<link href="https://fonts.googleapis.com/css2?family=Open+Sans:wght@400;600;700&family=Questrial&display=swap" rel="stylesheet">
<style>
:root{
  --bg:#f1f1f0;
  --ink:#3a3a3a;
  --text:#2b2b2b;
  --red:#9b1b1f;
  --card-dark:#1f1f1f;
  --paper:#f7f7f6;
  --white:#ffffff;
  --sig:#d9d9d9;
}
*{margin:0;padding:0;box-sizing:border-box}
html,body{width:1200px;height:744px;overflow:hidden;background:var(--bg)}
body{position:relative;font-family:"Open Sans",Arial,sans-serif;color:var(--text)}
.abs{position:absolute}

/* brand lockup */
.brand{display:flex;align-items:center}
.brand-square{background:var(--ink);flex:none}
.brand-name{font-family:"Open Sans",Arial,sans-serif;font-weight:600;color:var(--red);line-height:1;letter-spacing:.01em}
.tagline{font-family:"Questrial",Arial,sans-serif;color:var(--ink);white-space:nowrap}

.hero{left:57px;top:68px}
.hero .brand-square{width:50px;height:50px;margin-right:16px}
.hero .brand-name{font-size:66px}
.hero-tagline{left:127px;top:142px;font-size:11.5px;line-height:1}

/* business cards */
.card{width:145px;height:96px;box-shadow:0 2px 5px rgba(0,0,0,.25)}
.card-front{left:325px;top:295px;background:var(--card-dark)}
.card-front .brand{position:absolute;left:23px;top:35px}
.card-front .brand-square{width:14px;height:14px;margin-right:4px;background:var(--white)}
.card-front .brand-name{font-size:16px;color:var(--white)}
.card-front .tagline{position:absolute;left:42px;top:54px;font-size:3px;line-height:1;color:var(--white)}

.card-back{left:325px;top:425px;background:var(--white)}
.card-back .brand{position:absolute;right:8px;top:8px}
.card-back .brand-square{width:8px;height:8px;margin-right:3px}
.card-back .brand-name{font-size:10px}
.holder{position:absolute;left:5px;top:50px;font-size:4px;line-height:1.15}
.holder b{color:var(--red);font-weight:700}
.card-band{position:absolute;left:0;top:63px;width:100%;height:17px;background:var(--red);color:var(--white);font-size:3.2px;line-height:1.35}
.card-band .phones{position:absolute;left:6px;top:2px}
.card-band .web{position:absolute;left:68px;top:4.5px}
.card-address{position:absolute;left:6px;top:84px;font-size:3.3px}

/* letterhead */
.letter{left:520px;top:152px;width:260px;height:367px;background:var(--paper);box-shadow:0 4px 14px rgba(0,0,0,.22)}
.letter .brand{position:absolute;right:12px;top:9px}
.letter .brand-square{width:14px;height:14px;margin-right:4px}
.letter .brand-name{font-size:16px}
.letter .tagline{position:absolute;right:33px;top:27px;font-size:2.6px;line-height:1}
.letter-text{position:absolute;left:31px;font-size:4.6px;line-height:5.8px;width:185px}
.sender{top:73px;font-size:2.6px}
.recipient{top:88px}
.date{left:171px;top:119px;width:auto}
.subject{top:140px;font-weight:700}
.greeting{top:155px}
.para-1{top:167px}
.para-2{top:208px}
.closing{top:249px}
.signature{position:absolute;left:31px;top:258px;width:66px;height:10px;background:var(--sig);border-radius:2px}
.letter-footer{position:absolute;left:0;top:349px;width:100%;height:13px;background:var(--red);color:var(--white);font-size:2.1px;line-height:2.7px}
.letter-footer .col{position:absolute;top:2px;white-space:nowrap}
</style>
</head>
<body>

<section class="abs hero brand" aria-label="Talvera Wortmarke">
  <span class="brand-square"></span>
  <span class="brand-name">Talvera</span>
</section>
<p class="abs tagline hero-tagline">av solutions for professionals</p>

<article class="abs card card-front">
  <div class="brand"><span class="brand-square"></span><span class="brand-name">Talvera</span></div>
  <p class="tagline">av solutions for professionals</p>
</article>

<article class="abs card card-back">
  <div class="brand"><span class="brand-square"></span><span class="brand-name">Talvera</span></div>
  <p class="holder"><b>Lena Beispiel</b><br>Geschäftsführerin</p>
  <div class="card-band">
    <p class="phones">☏ +49 (0) 30 555 010 1<br>⎙ +49 (0) 30 555 010 2<br>▯ +49 (0) 170 555 010 300</p>
    <p class="web">info@talvera.de<br>www.talvera.de</p>
  </div>
  <p class="card-address"><b>Talvera</b> AV-Solutions | Beispielweg 4 | D - 54321 Beispielstadt</p>
</article>

<article class="abs letter">
  <div class="brand"><span class="brand-square"></span><span class="brand-name">Talvera</span></div>
  <p class="tagline">av solutions for professionals</p>

  <p class="letter-text sender"><b>Talvera</b> AV-Solutions | Beispielweg 4 | D-54321 Beispielstadt</p>
  <p class="letter-text recipient">Herrn<br>Jonas Beispiel<br>Beispielstraße 1<br>54321 Beispielstadt</p>
  <p class="letter-text date">Beispielstadt, 23.11.2015</p>
  <p class="letter-text subject">Betreff: Lorem Ipsum</p>
  <p class="letter-text greeting">Sehr geehrte Damen und Herren,</p>
  <p class="letter-text para-1">Lorem ipsum dolor sit amet, consetetur sadipscing elitr, sed diam nonumy eirmod tempor invidunt ut labore et dolore magna aliquyam erat, sed diam voluptua. At vero eos et accusam et justo duo dolores et ea rebum. Stet clita kasd gubergren, no sea takimata sanctus est Lorem ipsum dolor sit amet. Lorem ipsum dolor sit amet, consetetur sadipscing elitr, sed diam nonumy eirmod tempor</p>
  <p class="letter-text para-2">Duis autem vel eum iriure dolor in hendrerit in vulputate velit esse molestie consequat, vel illum dolore eu feugiat nulla facilisis at vero eros et accumsan et iusto odio dignissim qui blandit praesent luptatum zzril delenit augue duis dolore te feugait nulla facilisi. Lorem ipsum dolor sit amet.</p>
  <p class="letter-text closing">Mit freundlichen Grüßen</p>
  <div class="signature" role="img" aria-label="Handschriftliche Unterschrift von Lena Beispiel"></div>

  <footer class="letter-footer">
    <p class="col" style="left:31px"><b>Talvera</b> AV-Solutions<br>Beispielweg 4<br>D - 54321 Beispielstadt</p>
    <p class="col" style="left:67px"><b>Lena Beispiel</b><br>info@talvera.de<br>www.talvera.de</p>
    <p class="col" style="left:99px">☏ +49 (0) 30 555 010 1<br>⎙ +49 (0) 30 555 010 2<br>▯ +49 (0) 170 555 010 300</p>
    <p class="col" style="left:141px">Beispielbank Beispielstadt<br><b>IBAN</b> DE00 1234 5678<br><b>BIC</b> BEISDEXX</p>
    <p class="col" style="left:191px">Amtsgericht Beispielstadt<br>HRB 0000<br>USt-IdNr. DE000000</p>
  </footer>
</article>

</body>
</html>
```